Laser Engraving Business Needs Shopify Front and Backend Site Design

We are starting up a brick laser engraving business and need the Shopify front and back end created. The design will stylistically match the logo we had designed and is attached (specifically the embossed shadowed logo). The ideal design will be dark themed.

The back end will support a standard product template with the ability to group products by type. The design will also include the ability to track visitor interaction with the site, as well as links to the companies social media accounts. Billing will be handled through Shopify and linked to company accounts.
Updates

Project has been guaranteed and 2nd place money added. Project requirements were adjusted slightly to reflect feedback that was sent out. Great submissions so far!

Industry/Entity Type

Business

Font styles to use
Sans Serif

Colors
ec1f27

Requirements
Must have
• The design will stylistically match the logo we had designed and is attached and be dark overall.
• Front end must include an About Us, Products, Social Media, Custom Design.
• The back end will support modular products grouped by type.
Nice to have
• A Placeholder page supporting photos, video and blog type content.

```html
<!DOCTYPE html>
<html lang="en">
<head>
<meta charset="utf-8">
<title>Mason Mark — Brick Laser Engraving</title>
<link rel="stylesheet" href="https://fonts.googleapis.com/css2?family=Lato:wght@400;700;900&family=Open+Sans:wght@400;600;700&display=swap">
<style>
:root{
  --red:#ec1f27;
  --crimson:#a3182a;
  --crimson-dark:#7d1420;
  --ink:#2b2b2b;
  --charcoal:#333333;
  --slate:#3b3b3b;
  --night:#1f1f1f;
  --paper:#ffffff;
  --mist:#ececec;
  --line:#dddddd;
  --text:#555555;
  --muted:#999999;
  --gold:#f5a623;
  --brick:#8e4a35;
  --brick-light:#b8694a;
  --stone:#b59c7e;
  --sand:#d8b979;
}
*{box-sizing:border-box;margin:0;padding:0}
html,body{width:1200px;height:3944px;overflow:hidden}
body{font-family:"Open Sans",Arial,sans-serif;color:var(--text);background:var(--paper);font-size:13px}
.page{position:relative;width:1200px;height:3944px}
section,header,footer{position:absolute;left:0;width:1200px}
.abs{position:absolute}
.lato{font-family:"Lato",Arial,sans-serif}

/* top bar */
.topbar{top:0;height:32px;background:var(--crimson-dark);color:#f2d6d9;font-size:11px}
.topbar .left{left:100px;top:9px;display:flex;gap:22px}
.topbar .right{right:100px;top:9px;display:flex;gap:18px;align-items:center}
.topbar .dot{width:9px;height:9px;border-radius:50%;background:#e9b7bc;display:inline-block}

/* header */
.site-header{top:32px;height:128px;background:var(--ink)}
.brand{display:flex;align-items:center;gap:12px;font-family:"Lato",Arial,sans-serif;font-weight:900;color:var(--red);text-transform:uppercase;letter-spacing:1px}
.brand .mark{background:var(--red);display:inline-block}
.site-header .brand{left:100px;top:38px;font-size:34px}
.site-header .brand .mark{width:44px;height:44px}
.nav{right:100px;top:52px;display:flex;gap:44px;font-family:"Lato",Arial,sans-serif;font-weight:700;font-size:14px;color:#fff;align-items:center}
.nav .cart{display:flex;gap:8px;align-items:center}

/* hero */
.hero{top:160px;height:480px;background:linear-gradient(180deg,#3a1d16 0%,#6b3424 45%,#4a2419 100%)}
.hero-photo{position:absolute;inset:0;background:radial-gradient(ellipse at 50% 40%,rgba(160,80,55,.55),rgba(40,18,12,.7))}
.hero h1{position:absolute;top:150px;width:100%;text-align:center;font-family:"Lato",Arial,sans-serif;font-weight:900;font-size:58px;color:#fff;letter-spacing:3px}
.hero .sub{position:absolute;top:232px;width:100%;text-align:center;font-family:"Lato",Arial,sans-serif;font-size:24px;color:#fff;font-weight:700}
.hero .actions{position:absolute;top:290px;width:100%;display:flex;justify-content:center;gap:16px}
.btn{display:inline-block;font-family:"Lato",Arial,sans-serif;font-weight:700;font-size:12px;text-transform:uppercase;padding:12px 20px;color:#fff;letter-spacing:.5px}
.btn-red{background:var(--crimson)}
.btn-outline{border:1px solid #fff}
.btn-dark-outline{border:1px solid #333;color:#333;background:#fff}
.hero .arrow{position:absolute;top:220px}

/* about */
.about{top:640px;height:480px;background:var(--paper)}
.about .kicker{left:100px;top:80px;font-family:"Lato",Arial,sans-serif;font-weight:900;font-size:30px;color:var(--ink)}
.about h2{left:100px;top:118px;font-family:"Lato",Arial,sans-serif;font-weight:900;font-size:40px;color:var(--crimson)}
.about .rule{left:100px;top:174px;width:70px;height:3px;background:var(--crimson)}
.about p{left:100px;top:196px;width:380px;line-height:1.75;font-size:13px}
.about .btn{left:100px;top:340px}
.photo{position:absolute}
.about .p1{left:540px;top:70px;width:270px;height:330px;background:linear-gradient(135deg,#c7ab8c,#a58c70 60%,#8c735c)}
.about .p2{left:830px;top:70px;width:270px;height:330px;background:linear-gradient(160deg,#a4573f,#7e3e2c 60%,#c07050)}
.sq-arrow{position:absolute;width:26px;height:26px;background:#fff;border:1px solid #ccc;display:flex;align-items:center;justify-content:center}

/* daily deal */
.deal{top:1120px;height:560px;background:var(--slate)}
.deal .brand{left:100px;top:140px;font-size:58px}
.deal .brand .mark{width:74px;height:74px}
.deal .custom{left:100px;top:330px;font-family:"Lato",Arial,sans-serif;font-weight:900;font-size:28px;color:#fff}
.deal .custom-btn{left:100px;top:385px}
.deal h3{left:600px;top:72px;font-family:"Lato",Arial,sans-serif;font-weight:900;font-size:32px;color:#fff}
.deal .lead{left:600px;top:118px;font-size:20px;color:#fff}
.deal-item{position:absolute;top:160px;width:240px}
.deal-item .photo{position:relative;width:240px;height:260px}
.deal-item .name{color:#ddd;font-size:12px;margin-top:16px}
.deal-item .row{display:flex;justify-content:space-between;margin-top:8px;color:#fff;font-weight:700;font-size:14px}
.stars{color:var(--gold);font-size:13px;letter-spacing:1px}
.stars .off{color:#888}

/* products */
.products{top:1680px;height:720px;background:var(--paper)}
.section-title{position:absolute;width:100%;text-align:center;font-family:"Lato",Arial,sans-serif;font-weight:900;font-size:30px;color:var(--crimson)}
.section-sub{position:absolute;width:100%;text-align:center;font-size:12px;color:#777}
.tabs{position:absolute;top:175px;width:100%;display:flex;justify-content:center;gap:44px;font-family:"Lato",Arial,sans-serif;font-weight:700;font-size:13px;color:#333}
.tabs .active{color:var(--crimson);border-bottom:3px solid var(--crimson);padding-bottom:6px}
.card{position:absolute;top:250px;width:235px;text-align:center}
.card .photo{position:relative;width:235px;height:262px}
.card .stars{margin-top:16px}
.card .name{font-family:"Lato",Arial,sans-serif;font-weight:700;font-size:14px;color:#333;margin-top:6px}
.card .row{display:flex;justify-content:space-between;align-items:center;margin-top:14px;padding:0 12px}
.card .price{color:var(--crimson);font-weight:700;font-size:16px}
.card .btn{padding:8px 12px;font-size:11px}

/* news */
.news{top:2400px;height:680px;background:var(--mist)}
.post{position:absolute;top:180px;width:320px}
.post .photo{position:relative;width:320px;height:220px}
.post .cat{font-size:10px;color:#777;margin-top:18px;letter-spacing:.5px}
.post h4{font-family:"Lato",Arial,sans-serif;font-weight:900;font-size:15px;color:var(--crimson);margin-top:10px;line-height:1.3;text-transform:uppercase}
.post .date{font-size:12px;color:#555;margin-top:12px;display:flex;gap:8px;align-items:center}
.post p{font-size:12px;line-height:1.7;margin-top:14px}

/* widgets */
.widgets{top:3080px;height:360px;background:var(--slate);color:#ddd}
.widget-title{position:absolute;top:60px;font-family:"Lato",Arial,sans-serif;font-weight:900;font-size:20px;color:var(--red)}
.testimonial{position:absolute;left:100px;top:108px;width:290px}
.testimonial .who{display:flex;align-items:center;gap:14px}
.avatar{width:64px;height:64px;border-radius:50%;background:linear-gradient(135deg,#9a8574,#5e4d43)}
.testimonial .name{font-family:"Lato",Arial,sans-serif;font-weight:900;color:#fff;font-size:16px}
.testimonial .role{font-size:12px;color:#bbb}
.testimonial blockquote{margin-top:22px;font-size:13px;line-height:1.7;color:#ddd;padding-left:24px;position:relative}
.testimonial blockquote:before{content:"\201C";position:absolute;left:0;top:-8px;font-size:36px;color:#fff}
.mini-list{position:absolute;top:108px;display:flex;flex-direction:column;gap:18px}
.mini{display:flex;gap:14px;align-items:center}
.mini .thumb{width:54px;height:54px}
.mini .t{font-size:12px;color:#fff}
.mini .p{font-size:12px;color:#fff;font-weight:700;margin-top:2px}
.mini .a{font-size:11px;color:#fff;margin-top:2px}

/* footer */
.site-footer{top:3440px;height:440px;background:var(--ink);color:#ccc}
.site-footer .divider{left:100px;top:0;width:1000px;height:1px;background:#555}
.site-footer .brand{left:100px;top:60px;font-size:26px}
.site-footer .brand .mark{width:32px;height:32px}
.site-footer .intro{left:100px;top:110px;width:320px;font-weight:700;color:#fff;font-size:12px;line-height:1.6}
.contact{left:100px;top:172px;display:flex;flex-direction:column;gap:10px;font-size:12px;color:#fff}
.contact div{display:flex;gap:10px;align-items:center}
.fcol{position:absolute;top:60px}
.fcol h5{font-family:"Lato",Arial,sans-serif;font-weight:900;font-size:15px;color:var(--red);text-transform:uppercase;margin-bottom:16px}
.fcol li{list-style:none;font-size:12px;color:#ccc;line-height:2}
.site-footer .copy{left:100px;top:358px;font-size:12px;color:#aaa}
.socials{right:100px;top:348px;display:flex;gap:8px}
.socials span{width:30px;height:30px;border-radius:50%;border:1px solid #999;display:inline-block}
.site-footer .bottom-rule{left:100px;top:330px;width:1000px;height:1px;background:#444}

/* newsletter */
.newsletter{top:3880px;height:64px;background:var(--night);color:#fff}
.newsletter .label{left:100px;top:23px;font-family:"Lato",Arial,sans-serif;font-weight:900;font-size:13px}
.newsletter .field{left:210px;top:16px;width:250px;height:32px;background:#fff;color:#999;font-size:11px;padding:9px 12px}
.newsletter .btn{left:476px;top:16px;padding:9px 18px;font-size:11px}
.pay{right:100px;top:20px;display:flex;gap:8px}
.pay span{width:40px;height:24px;background:#e6e6e6;border-radius:3px;display:inline-block}
</style>
</head>
<body>
<div class="page">

  <div class="topbar abs" style="top:0;left:0;width:1200px">
    <div class="abs left"><span>EN</span><span>USD</span><span>EUR</span></div>
    <div class="abs right">
      <span class="dot"></span><span class="dot"></span><span class="dot"></span><span class="dot"></span>
      <span>Register / Login</span>
    </div>
  </div>

  <header class="site-header">
    <div class="abs brand"><span class="mark"></span>Mason Mark</div>
    <nav class="abs nav">
      <span>HOME</span><span>ABOUT US</span><span>PRODUCTS</span><span>CONTACT</span>
      <span class="cart">
        <svg width="20" height="18" viewBox="0 0 20 18" fill="none" stroke="#fff" stroke-width="1.6"><path d="M1 1h3l2 11h11l2-8H5"/><circle cx="8" cy="16" r="1.3"/><circle cx="15" cy="16" r="1.3"/></svg>
        CART 0
      </span>
    </nav>
  </header>

  <section class="hero">
    <div class="hero-photo" role="img" aria-label="Dark red brick wall photograph"></div>
    <h1>MASON MARK</h1>
    <div class="sub">Brick Laser Engraving</div>
    <div class="actions"><span class="btn btn-red">Read More</span><span class="btn btn-outline">Contact Us</span></div>
    <svg class="arrow" style="left:30px" width="16" height="30" viewBox="0 0 16 30"><path d="M14 2L2 15l12 13" stroke="#fff" stroke-width="2.5" fill="none"/></svg>
    <svg class="arrow" style="right:30px" width="16" height="30" viewBox="0 0 16 30"><path d="M2 2l12 13L2 28" stroke="#fff" stroke-width="2.5" fill="none"/></svg>
  </section>

  <section class="about">
    <div class="abs kicker">ABOUT</div>
    <h2 class="abs">MASON MARK</h2>
    <div class="abs rule"></div>
    <p class="abs">Nemo enim ipsam voluptatem quia voluptas sit aspernatur aut odit aut fugit, sed quia consequuntur magni dolores eos qui ratione voluptatem sequi nesciunt. Neque porro quisquam est, qui dolorem ipsum quia dolor sit amet, consectetur, adipisci velit, sed quia non numquam eius modi tempora incidunt ut labore et dolore magnam aliquam quaerat voluptatem.</p>
    <span class="abs btn btn-red">Read More</span>
    <div class="photo p1" role="img" aria-label="Engraved sandstone wall detail"></div>
    <div class="photo p2" role="img" aria-label="Carved red brick facade"></div>
    <span class="sq-arrow" style="left:527px;top:222px"><svg width="8" height="12"><path d="M7 1L2 6l5 5" stroke="#555" stroke-width="1.6" fill="none"/></svg></span>
    <span class="sq-arrow" style="left:1087px;top:222px"><svg width="8" height="12"><path d="M1 1l5 5-5 5" stroke="#555" stroke-width="1.6" fill="none"/></svg></span>
  </section>

  <section class="deal">
    <div class="abs brand"><span class="mark"></span>Mason Mark</div>
    <div class="abs custom">NEED A CUSTOM DESIGN</div>
    <span class="abs btn btn-outline custom-btn">Click Here</span>
    <h3 class="abs">DAILY DEAL</h3>
    <div class="abs lead">Deals 35% for all JACKETS products.</div>
    <div class="deal-item" style="left:600px">
      <div class="photo" role="img" aria-label="Engraved stone lettering product" style="background:linear-gradient(140deg,#c9a77c,#a2835f)"></div>
      <div class="name">Nemo enim ipsam</div>
      <div class="row"><span>$200.00</span><span class="stars">★★★<span class="off">★★</span></span></div>
    </div>
    <div class="deal-item" style="left:860px">
      <div class="photo" role="img" aria-label="Red brick wall product" style="background:linear-gradient(160deg,#b0604a,#874433)"></div>
      <div class="name">Nemo enim ipsam</div>
      <div class="row"><span>$260.00</span><span class="stars">★★★<span class="off">★★</span></span></div>
    </div>
  </section>

  <section class="products">
    <div class="section-title" style="top:72px">OUR PRODUCTS</div>
    <div class="section-sub" style="top:118px">Lorem Ipsum is simply dummy text of the printing and typesetting industry.</div>
    <div class="tabs"><span class="active">ALL</span><span>TOP RATED</span><span>FEATURED</span><span>BRICK</span><span>ACCESSORIES</span></div>

    <div class="card" style="left:100px">
      <div class="photo" role="img" aria-label="Orange clay bricks" style="background:linear-gradient(150deg,#c5603e,#9b4128)"></div>
      <div class="stars">★★★★<span class="off">★</span></div>
      <div class="name">FUSCE ALIQUAM</div>
      <div class="row"><span class="price">$650.00</span><span class="btn btn-red">Add to cart</span></div>
    </div>
    <div class="card" style="left:355px">
      <div class="photo" role="img" aria-label="Square brick lattice" style="background:linear-gradient(150deg,#b06a3a,#7c4320)"></div>
      <div class="stars">★★★★<span class="off">★</span></div>
      <div class="name">FUSCE ALIQUAM</div>
      <div class="row"><span class="price">$650.00</span><span class="btn btn-dark-outline">Add to cart</span></div>
    </div>
    <div class="card" style="left:610px">
      <div class="photo" role="img" aria-label="Radial brick paving" style="background:radial-gradient(circle at 55% 45%,#c9914f,#8a5527)"></div>
      <div class="stars">★★★★<span class="off">★</span></div>
      <div class="name">FUSCE ALIQUAM</div>
      <div class="row"><span class="price">$650.00</span><span class="btn btn-dark-outline">Add to cart</span></div>
    </div>
    <div class="card" style="left:865px">
      <div class="photo" role="img" aria-label="Brown brick grid" style="background:linear-gradient(150deg,#a26a3c,#6b4226)"></div>
      <div class="stars">★★★★<span class="off">★</span></div>
      <div class="name">FUSCE ALIQUAM</div>
      <div class="row"><span class="price">$650.00</span><span class="btn btn-dark-outline">Add to cart</span></div>
    </div>
    <span class="sq-arrow" style="left:87px;top:368px"><svg width="8" height="12"><path d="M7 1L2 6l5 5" stroke="#555" stroke-width="1.6" fill="none"/></svg></span>
    <span class="sq-arrow" style="left:1087px;top:368px"><svg width="8" height="12"><path d="M1 1l5 5-5 5" stroke="#555" stroke-width="1.6" fill="none"/></svg></span>
  </section>

  <section class="news">
    <div class="section-title" style="top:72px">NEWS &amp; BLOG</div>
    <div class="section-sub" style="top:118px">Lorem Ipsum is simply dummy text of the printing and typesetting industry.</div>
    <div class="post" style="left:100px">
      <div class="photo" role="img" aria-label="Diamond pattern brickwork" style="background:linear-gradient(135deg,#e0c27e,#c9a35a)"></div>
      <div class="cat">POSTED IN NEWS</div>
      <h4>Perspiciatis unde omnis iste natus error sit</h4>
      <div class="date"><svg width="12" height="12" viewBox="0 0 12 12" fill="none" stroke="#555"><rect x="1" y="2" width="10" height="9"/><path d="M1 5h10M4 1v2M8 1v2"/></svg>07 September, 2017</div>
      <p>Nemo enim ipsam voluptatem quia voluptas sit aspernatur aut odit aut fugit.</p>
    </div>
    <div class="post" style="left:440px">
      <div class="photo" role="img" aria-label="Carved stone building facade" style="background:linear-gradient(160deg,#a89274,#6f5c48)"></div>
      <div class="cat">POSTED IN NEWS</div>
      <h4>Perspiciatis unde omnis iste natus error sit</h4>
      <div class="date"><svg width="12" height="12" viewBox="0 0 12 12" fill="none" stroke="#555"><rect x="1" y="2" width="10" height="9"/><path d="M1 5h10M4 1v2M8 1v2"/></svg>07 September, 2017</div>
      <p>Nemo enim ipsam voluptatem quia voluptas sit aspernatur aut odit aut fugit.</p>
    </div>
    <div class="post" style="left:780px">
      <div class="photo" role="img" aria-label="Old brick street wall" style="background:linear-gradient(160deg,#9b5a3e,#5e3526)"></div>
      <div class="cat">POSTED IN NEWS</div>
      <h4>Perspiciatis unde omnis iste natus error sit</h4>
      <div class="date"><svg width="12" height="12" viewBox="0 0 12 12" fill="none" stroke="#555"><rect x="1" y="2" width="10" height="9"/><path d="M1 5h10M4 1v2M8 1v2"/></svg>07 September, 2017</div>
      <p>Nemo enim ipsam voluptatem quia voluptas sit aspernatur aut odit aut fugit.</p>
    </div>
  </section>

  <section class="widgets">
    <div class="widget-title" style="left:100px">TESTIMONIAL</div>
    <div class="testimonial">
      <div class="who"><div class="avatar" role="img" aria-label="Customer portrait"></div><div><div class="name">JOHN DOE</div><div class="role">- Manager</div></div></div>
      <blockquote>Nemo enim ipsam voluptatem quia voluptas sit aspernatur aut odit aut fugit sed quia consequuntur.</blockquote>
    </div>

    <div class="widget-title" style="left:430px">NEW ARRIVALS</div>
    <div class="mini-list" style="left:430px">
      <div class="mini"><div class="thumb" role="img" aria-label="Engraved brick" style="background:#b4764d"></div><div><div class="t">Nemo Enim</div><div class="p">$75.00</div><div class="a">+ Add To Cart</div></div></div>
      <div class="mini"><div class="thumb" role="img" aria-label="Stone tile" style="background:#c9a97e"></div><div><div class="t">Nemo Enim</div><div class="p">$75.00</div><div class="a">+ Add To Cart</div></div></div>
      <div class="mini"><div class="thumb" role="img" aria-label="Red brick" style="background:#9e4a34"></div><div><div class="t">Nemo Enim</div><div class="p">$75.00</div><div class="a">+ Add To Cart</div></div></div>
    </div>

    <div class="widget-title" style="left:680px">BESTSELLER</div>
    <div class="mini-list" style="left:680px">
      <div class="mini"><div class="thumb" role="img" aria-label="Brick pattern" style="background:#a8653f"></div><div><div class="t">Nemo Enim</div><div class="p">$75.00</div><div class="a">+ Add To Cart</div></div></div>
      <div class="mini"><div class="thumb" role="img" aria-label="Stone tile" style="background:#bfa27c"></div><div><div class="t">Nemo Enim</div><div class="p">$75.00</div><div class="a">+ Add To Cart</div></div></div>
      <div class="mini"><div class="thumb" role="img" aria-label="Red brick" style="background:#8f4632"></div><div><div class="t">Nemo Enim</div><div class="p">$75.00</div><div class="a">+ Add To Cart</div></div></div>
    </div>

    <div class="widget-title" style="left:930px">FEATURED</div>
    <div class="mini-list" style="left:930px">
      <div class="mini"><div class="thumb" role="img" aria-label="Engraved brick" style="background:#b87a4f"></div><div><div class="t">Nemo Enim</div><div class="p">$75.00</div><div class="a">+ Add To Cart</div></div></div>
      <div class="mini"><div class="thumb" role="img" aria-label="Stone tile" style="background:#cdb08a"></div><div><div class="t">Nemo Enim</div><div class="p">$75.00</div><div class="a">+ Add To Cart</div></div></div>
      <div class="mini"><div class="thumb" role="img" aria-label="Red brick" style="background:#a0503a"></div><div><div class="t">Nemo Enim</div><div class="p">$75.00</div><div class="a">+ Add To Cart</div></div></div>
    </div>
  </section>

  <footer class="site-footer">
    <div class="abs divider"></div>
    <div class="abs brand"><span class="mark"></span>Mason Mark</div>
    <div class="abs intro">Lorem Ipsum is simply dummy text of the printing and typesetting industry.</div>
    <div class="abs contact">
      <div><svg width="12" height="12" viewBox="0 0 12 12" fill="#fff"><path d="M2 1h3l1 3-2 1a7 7 0 003 3l1-2 3 1v3c-6 1-10-3-9-9z"/></svg>Telephone: (555) 014-2290</div>
      <div><svg width="12" height="10" viewBox="0 0 12 10" fill="none" stroke="#fff"><rect x=".5" y=".5" width="11" height="9"/><path d="M.5 .5l5.5 5 5.5-5"/></svg>Email: hello@masonmark.example</div>
      <div><svg width="12" height="12" viewBox="0 0 12 12" fill="none" stroke="#fff"><circle cx="6" cy="6" r="5"/><path d="M6 3v3l2 1"/></svg>8:00 - 19:00, Monday - Saturday, Sunday - closed</div>
    </div>
    <div class="fcol" style="left:530px"><h5>Information</h5><ul><li>Help</li><li>Contact Us</li><li>Warranty</li><li>Terms &amp; Conditions</li><li>Shopping Information</li></ul></div>
    <div class="fcol" style="left:780px"><h5>Service</h5><ul><li>My Account</li><li>Order Status</li><li>Payment</li><li>Gift Voucher</li><li>Cancellations</li></ul></div>
    <div class="fcol" style="left:970px"><h5>My Account</h5><ul><li>Projects</li><li>Jobs</li><li>Collections</li><li>Blog</li><li>Media</li></ul></div>
    <div class="abs bottom-rule"></div>
    <div class="abs copy">Copyright 2017 Mason Mark. All Rights Reserved</div>
    <div class="abs socials"><span></span><span></span><span></span><span></span><span></span></div>
  </footer>

  <section class="newsletter">
    <div class="abs label">NEWSLETTER</div>
    <div class="abs field">email@example.com</div>
    <span class="abs btn btn-red">Subscribe</span>
    <div class="abs pay"><span></span><span></span><span></span><span></span><span></span></div>
  </section>

</div>
</body>
</html>
```